Business Card for Inovative Flexible Packaging Company

Create a business card that is both simple and stricking at the same time.
Preferably only one color (orange) or two colors (black and orange).
Information to print:
Corvela, Lda
[T] 22 418 6093
[M] 91 362 7148
[F] 22 418 6057
[@] corvela.mt@tarnomail.example
SEDE & ARMAZÉM
Rua Dos Vimieiros do Outeiro, 317
Serzedo
4410-862 Serzedo - VN Gaia
PORTUGAL
Reason: A lot of the ideas are obvious. I want something different. Inovative. dare to do something eye catching with style.
Business Consumers. Packaging Designers.
Business

```html
<!DOCTYPE html>
<html lang="pt">
<head>
<meta charset="utf-8">
<title>Corvela business card</title>
<link rel="stylesheet" href="https://fonts.googleapis.com/css2?family=Questrial&display=swap">
<style>
  :root {
    --bg: #1a1a1a;
    --card: #050505;
    --orange: #ff8a00;
    --orange-deep: #e86a00;
    --panel-a: #3a1e05;
    --panel-b: #0c0603;
    --text: #f2f2f2;
  }
  * { margin: 0; padding: 0; box-sizing: border-box; }
  html, body { width: 1200px; height: 675px; overflow: hidden; }
  body {
    background: var(--bg);
    font-family: "Questrial", "Century Gothic", sans-serif;
    display: flex; align-items: center; justify-content: center; gap: 40px;
  }
  .card {
    position: relative; width: 560px; height: 320px;
    background: var(--card); overflow: hidden;
    box-shadow: 0 10px 30px rgba(0,0,0,.6);
  }
  .wordmark {
    display: flex; align-items: center; gap: 14px;
    color: var(--orange); letter-spacing: .5px;
  }
  .wordmark .mark-square { background: var(--orange); display: block; }
  .card-front .wordmark {
    position: absolute; left: 50%; top: 50%; transform: translate(-50%,-50%);
    font-size: 76px;
  }
  .card-front .mark-square { width: 54px; height: 54px; }

  .card-back .side-panel {
    position: absolute; left: 0; top: 0; width: 300px; height: 320px;
    background: linear-gradient(135deg, var(--panel-a), var(--panel-b) 75%);
  }
  .card-back .wordmark {
    position: absolute; left: 40px; top: 58px; font-size: 44px; gap: 10px;
  }
  .card-back .mark-square { width: 30px; height: 30px; }
  .contact-list {
    position: absolute; left: 40px; top: 170px; list-style: none;
    color: var(--text); font-size: 15px; line-height: 27px;
  }
  .contact-list li { display: flex; align-items: center; gap: 14px; }
  .contact-list svg { width: 16px; height: 16px; fill: var(--orange); flex: none; }
  .company-name {
    position: absolute; right: 34px; top: 40px;
    color: var(--orange); font-size: 18px; font-weight: 700;
  }
  .address {
    position: absolute; right: 34px; top: 138px; text-align: right;
    color: var(--text); font-size: 14px; line-height: 22px; font-style: normal;
  }
  .address .label { color: var(--orange); font-size: 12px; font-weight: 700; letter-spacing: .3px; }
</style>
</head>
<body>
  <section class="card card-front">
    <div class="wordmark"><span class="mark-square"></span>corvela</div>
  </section>

  <section class="card card-back">
    <div class="side-panel"></div>
    <div class="wordmark"><span class="mark-square"></span>corvela</div>
    <ul class="contact-list">
      <li><svg viewBox="0 0 16 16" aria-hidden="true"><path d="M2 5c0-2 2-3 6-3s6 1 6 3l-3 1-1-2H6L5 6zM4 8h8l2 6H2z"/></svg>22 418 6093</li>
      <li><svg viewBox="0 0 16 16" aria-hidden="true"><path d="M5 1h6a1 1 0 0 1 1 1v12a1 1 0 0 1-1 1H5a1 1 0 0 1-1-1V2a1 1 0 0 1 1-1zm1 2v8h4V3z"/></svg>91 362 7148</li>
      <li><svg viewBox="0 0 16 16" aria-hidden="true"><path d="M4 1h7v4H4zM2 6h12v7H2zm3 2v2h6V8zM4 14h8v1H4z"/></svg>22 418 6057</li>
      <li><svg viewBox="0 0 16 16" aria-hidden="true"><path d="M1 3h14v10H1zm1.5 1.5L8 9l5.5-4.5z" fill-rule="evenodd"/></svg>corvela.mt@tarnomail.example</li>
    </ul>
    <p class="company-name">Corvela, Lda</p>
    <address class="address">
      <span class="label">SEDE &amp; ARMAZÉM</span><br>
      Rua Dos Vimieiros do Outeiro, 317<br>
      Serzedo<br>
      4410-862 Serzedo - VN Gaia<br>
      PORTUGAL
    </address>
  </section>
</body>
</html>
```